An animal window cleaning business card

I want a business card design that includes a logo and tells people I am a WINDOW WASHING COMPANY right away.
Were based in Maine, we do window cleaning, pressure washing, and gutter cleaning. We like Pine trees, the Ocean, state of Maine symbols, Lobsters, Moose, Huskies, etc. My business name is "BRIGHT PANE WINDOWS"
The card could also be designed to look like a gift credit card with a 50$ value.

Target Market(s)

my target audience is older folks with disposable money who live on the ocean or have secondary homes for vacation in Maine

Industry/Entity Type

Cleaning Services

Contact Information for Business Card

2.5x3" plastic if possible.

Font styles to use
Sans Serif

Requirements
Must have
• a symbol, or a logo that tells people I am a window washing company Instantly.
The words BRIGHT PANE, my phone number, my name, MY email
Nice to have
• a lobster holding a squeegee, or a stylized cartoonish version of a human huskie holding a squeegee,
Should not have
• a lighthouse
small hard to read text

```html
<!DOCTYPE html>
<html lang="en">
<head>
<meta charset="utf-8">
<title>Bright Pane Windows – Business Card</title>
<link rel="stylesheet" href="https://fonts.googleapis.com/css2?family=Bebas+Neue&family=Kaushan+Script&family=Lato:ital,wght@0,400;0,700;1,400&display=swap">
<style>
  :root {
    --bg: #e9ecef;
    --sky-light: #eaf6fd;
    --sky-mid: #b5def6;
    --title-blue: #1a8fd0;
    --deep-blue: #0b4fb0;
    --contact-blue: #1a55b0;
    --ink: #111111;
    --back-top: #2384ba;
    --back-bottom: #7bc9ec;
    --white: #ffffff;
  }
  * { box-sizing: border-box; margin: 0; padding: 0; }
  html, body { width: 963px; height: 1200px; overflow: hidden; }
  body { background: var(--bg); position: relative; font-family: "Lato", sans-serif; }

  .card {
    position: absolute;
    left: 224px;
    width: 576px;
    height: 330px;
    border-radius: 18px;
    overflow: hidden;
  }
  .card--front {
    top: 214px;
    background: linear-gradient(160deg, var(--sky-light) 0%, var(--sky-mid) 60%, #d8effb 100%);
  }
  .card--back {
    top: 627px;
    background: linear-gradient(180deg, var(--back-top) 0%, var(--back-bottom) 100%);
  }

  .worker-art {
    position: absolute;
    left: 6px; top: 118px;
    width: 228px; height: 212px;
    background: linear-gradient(180deg, #1c2a36 0%, #0c1218 100%);
    border-radius: 50% 50% 0 0 / 34% 34% 0 0;
  }
  .splash-art {
    position: absolute;
    left: 200px; top: 150px;
    width: 376px; height: 180px;
    background: radial-gradient(ellipse at 70% 30%, rgba(30,130,210,0.55) 0%, rgba(120,190,240,0.25) 45%, rgba(255,255,255,0) 75%);
  }

  .front-title {
    position: absolute;
    left: 188px; top: 40px;
    font-family: "Bebas Neue", sans-serif;
    font-weight: 400;
    font-size: 50px;
    line-height: 1;
    letter-spacing: 0.3px;
    color: var(--title-blue);
    white-space: nowrap;
  }

  .value-badge {
    position: absolute;
    left: 390px; top: 90px;
    width: 136px; height: 136px;
  }
  .value-badge svg { display: block; }
  .value-badge__amount {
    position: absolute;
    inset: 0;
    display: flex; align-items: center; justify-content: center;
    font-family: "Bebas Neue", sans-serif;
    font-size: 60px;
    color: var(--white);
    padding-top: 6px;
  }

  .owner-name {
    position: absolute;
    right: 46px; top: 222px;
    font-family: "Kaushan Script", cursive;
    font-size: 36px;
    line-height: 1.1;
    color: var(--ink);
    white-space: nowrap;
  }
  .owner-phone {
    position: absolute;
    right: 46px; top: 270px;
    font-weight: 700;
    font-size: 28px;
    line-height: 1.1;
    color: var(--contact-blue);
  }
  .owner-email {
    position: absolute;
    right: 46px; top: 305px;
    font-style: italic;
    font-size: 14.5px;
    line-height: 1.1;
    color: var(--contact-blue);
  }

  .water-art {
    position: absolute;
    left: 0; top: 0; width: 100%; height: 100%;
    background: radial-gradient(ellipse at 80% 20%, rgba(255,255,255,0.18) 0%, rgba(255,255,255,0) 55%),
                radial-gradient(ellipse at 30% 55%, rgba(255,255,255,0.12) 0%, rgba(255,255,255,0) 50%);
  }
  .back-title {
    position: absolute;
    left: 0; right: 0; top: 124px;
    text-align: center;
    font-family: "Bebas Neue", sans-serif;
    font-weight: 400;
    font-size: 38px;
    line-height: 1;
    color: var(--white);
  }
  .service-list {
    position: absolute;
    left: 0; right: 0; top: 172px;
    text-align: center;
    font-size: 13.5px;
    line-height: 16px;
    color: var(--white);
  }
  .service-list .dot { margin: 0 6px; font-size: 10px; }
</style>
</head>
<body>
  <section class="card card--front">
    <div class="splash-art" role="img" aria-label="Blue water splash with bubbles"></div>
    <div class="worker-art" role="img" aria-label="Silhouette of a window cleaner raising a squeegee"></div>
    <h1 class="front-title">BRIGHT PANE WINDOWS</h1>
    <div class="value-badge">
      <svg viewBox="0 0 140 140" width="136" height="136" aria-hidden="true">
        <g fill="var(--deep-blue)">
          <rect x="22" y="22" width="96" height="96" transform="rotate(0 70 70)"/>
          <rect x="22" y="22" width="96" height="96" transform="rotate(15 70 70)"/>
          <rect x="22" y="22" width="96" height="96" transform="rotate(30 70 70)"/>
          <rect x="22" y="22" width="96" height="96" transform="rotate(45 70 70)"/>
          <rect x="22" y="22" width="96" height="96" transform="rotate(60 70 70)"/>
          <rect x="22" y="22" width="96" height="96" transform="rotate(75 70 70)"/>
        </g>
      </svg>
      <span class="value-badge__amount">50$</span>
    </div>
    <p class="owner-name">Daniel Harper</p>
    <p class="owner-phone">207-555-0148</p>
    <p class="owner-email">info@brightpanewindows.com</p>
  </section>

  <section class="card card--back">
    <div class="water-art" role="img" aria-label="Soft flowing water texture"></div>
    <h2 class="back-title">BRIGHT PANE WINDOWS</h2>
    <p class="service-list">
      Window Washing<span class="dot">●</span>Gutter Cleaning<span class="dot">●</span>Leaf Filter Installation<br>
      Pressure Washing<span class="dot">●</span>Roof Cleaning
    </p>
  </section>
</body>
</html>
```